Velvet Basin Suites, a portable luxury restroom trailer company needs a landing page

We need a landing page for a luxury portable restroom trailer company. This should be modern, and simple - use any combination of Pantone colors: Warm Gray 1C, Black 7C, 7529c, 873C, 8003C

We rent these trailers for special events like weddings, private parties, festivals, family reunions, team building, wine tastings, beer tastings, food truck round-ups, etc.

An idea of the landing page is in the files below. Please use stock photography and placeholder text for now. The winning design will be given final content.

Requirements
Must have
• Multiple "Get Quote" buttons or a place for them to type in type of rental, how many people etc

```html
<!DOCTYPE html>
<html lang="en">
<head>
<meta charset="utf-8">
<title>Velvet Basin Suites — Luxury Restroom Trailers</title>
<link href="https://fonts.googleapis.com/css2?family=Poppins:wght@400;500;600;800&family=Oswald:wght@400&family=Lato:wght@400;700&display=swap" rel="stylesheet">
<style>
:root{
  --gold:#c9992c;
  --dark:#2b2a29;
  --darker:#232221;
  --light:#f4f3f1;
  --warm:#e7e4df;
  --text:#4a4a4a;
  --red:#d83a2a;
  --white:#fff;
}
*{box-sizing:border-box;margin:0;padding:0}
html,body{width:1200px;height:3929px;overflow:hidden;background:var(--white)}
body{position:relative;font-family:"Lato",sans-serif;color:var(--text)}
.abs{position:absolute}
.brand-box{position:absolute;background:var(--white);display:flex;flex-direction:column;align-items:center;justify-content:center;gap:6px}
.brand-box .dot{width:34px;height:34px;border-radius:50%;background:var(--gold)}
.brand-box .name{font-family:"Poppins",sans-serif;font-weight:500;font-size:11px;color:var(--gold);text-align:center;line-height:1.1}
.nav{position:absolute;display:flex;font-family:"Poppins",sans-serif;font-size:14px;color:var(--white);font-weight:500}
.nav span{position:absolute;white-space:nowrap}
.nav .active{color:var(--gold)}
.btn{position:absolute;background:var(--gold);color:var(--white);font-family:"Poppins",sans-serif;font-weight:500;letter-spacing:1.5px;display:flex;align-items:center;justify-content:center;gap:6px;text-transform:uppercase}
.btn svg{width:14px;height:14px}
.photo{position:absolute}
h2{font-family:"Poppins",sans-serif;font-weight:600;color:var(--dark);position:absolute;text-align:center}
.card-title{position:absolute;font-family:"Oswald",sans-serif;font-size:19px;color:var(--dark);text-align:center;width:300px}
.card-text{position:absolute;font-family:"Poppins",sans-serif;font-size:11.5px;line-height:20px;color:var(--text);text-align:center;width:280px}
.read{position:absolute;font-family:"Poppins",sans-serif;font-size:10px;font-weight:600;color:var(--red);letter-spacing:1.5px;text-align:center;width:200px}
.feat-icon{position:absolute;width:80px;height:80px;border-radius:50%;background:var(--gold);display:flex;align-items:center;justify-content:center}
.feat-icon svg{width:38px;height:38px}
.feat-title{position:absolute;font-family:"Oswald",sans-serif;font-size:18px;color:var(--dark);line-height:29px;width:200px}
.feat-text{position:absolute;font-family:"Lato",sans-serif;font-size:11.5px;line-height:20px;color:var(--text);width:165px}
.right{text-align:right}
.field-label{position:absolute;font-family:"Lato",sans-serif;font-size:11px;color:var(--white)}
.field{position:absolute;background:var(--white);border:2px solid var(--gold);border-radius:3px;font-family:"Lato",sans-serif;font-size:11px;color:#888;padding:0 10px;display:flex;align-items:center}
.info-title{position:absolute;font-family:"Oswald",sans-serif;font-size:19px;color:var(--dark)}
.info-text{position:absolute;font-family:"Poppins",sans-serif;font-size:12.5px;color:var(--text);line-height:21px}
.info-icon{position:absolute;width:38px;height:38px;border-radius:50%;background:var(--gold);display:flex;align-items:center;justify-content:center}
.info-icon svg{width:18px;height:18px}
</style>
</head>
<body>

<header class="abs" style="left:0;top:0;width:1200px;height:100px;background:var(--dark)">
  <div class="brand-box" style="left:41px;top:0;width:116px;height:88px"><div class="dot"></div><div class="name">VELVET BASIN<br>SUITES</div></div>
  <nav class="nav" style="left:0;top:30px">
    <span class="active" style="left:400px">HOME</span>
    <span style="left:473px">ABOUT US</span>
    <span style="left:575px">OUR PRODUCTS</span>
    <span style="left:714px">CONTACT US</span>
  </nav>
  <div class="abs" style="left:382px;top:52px;width:75px;height:2px;background:var(--gold)"></div>
  <div class="btn" style="left:1000px;top:20px;width:177px;height:40px;font-size:14px;border:1px solid #e0b850"><svg viewBox="0 0 14 14" fill="none" stroke="#fff" stroke-width="2"><path d="M2 3l4 4-4 4M7 3l4 4-4 4"/></svg>GET A QUOTE</div>
  <div class="abs" style="left:0;top:92px;width:1200px;height:8px;background:var(--gold)"></div>
</header>

<section class="abs" style="left:0;top:100px;width:1200px;height:598px;background:var(--dark)">
  <div class="photo" role="img" aria-label="Row of white and teal portable toilets standing on snow" style="left:0;top:0;width:1200px;height:586px;background:linear-gradient(180deg,#e9eef1 0%,#2f8aa6 35%,#dfe6ea 60%,#f3f4f5 100%);clip-path:polygon(465px 0,1200px 0,1200px 586px,600px 586px)"></div>
  <svg class="abs" style="left:0;top:0" width="1200" height="586"><polygon points="0,0 443,0 578,586 0,586" fill="var(--dark)"/><polygon points="443,0 465,0 600,586 578,586" fill="var(--gold)"/></svg>
  <div class="abs" style="left:459px;top:243px;width:128px;height:128px;border-radius:50%;background:var(--white);border:6px solid var(--gold)"></div>
  <div class="abs" style="left:40px;top:156px;font-family:'Poppins',sans-serif;font-weight:800;font-size:43px;line-height:43px;color:var(--white)">We Are The Leader<br>In Portable Toilet<br>&amp; Restroom Trailer<br>Services!</div>
  <div class="abs" style="left:40px;top:352px;font-family:'Lato',sans-serif;font-size:12.5px;color:var(--white)">Lorem ipsum dolor sit amet consectetur adipiscing elit dolor</div>
  <div class="btn" style="left:40px;top:394px;width:137px;height:37px;font-size:11px;letter-spacing:0;border:2px solid #e5c26b;border-radius:4px">EXPLORE MORE</div>
  <svg class="abs" style="left:12px;top:286px" width="12" height="18" fill="none" stroke="#fff" stroke-width="2"><path d="M9 2L3 9l6 7"/></svg>
  <svg class="abs" style="left:1176px;top:286px" width="12" height="18" fill="none" stroke="#fff" stroke-width="2"><path d="M3 2l6 7-6 7"/></svg>
</section>

<section class="abs" style="left:0;top:698px;width:1200px;height:870px">
  <h2 style="left:0;top:62px;width:1200px;font-size:31px">Our Products</h2>
  <p class="abs" style="left:45px;top:120px;width:1110px;text-align:center;font-family:'Poppins',sans-serif;font-size:12px;line-height:20px">Lorem ipsum dolor sit amet, consectetur adipiscing elit, sed do eiusmod tempor incididunt ut labore et dolore magna aliqua. Ut enim ad minim veniam, quis nostrud exercitation ullamco laboris nisi ut aliquip ex ea commodo consequat. Duis aute irure dolor in reprehenderit in voluptate velit esse cillum dolore eu fugiat nulla pariatur.</p>

  <div class="photo" role="img" aria-label="Blue portable restroom unit" style="left:558px;top:202px;width:92px;height:175px;background:linear-gradient(180deg,#4f79a8,#2f5582)"></div>
  <div class="card-title" style="left:450px;top:397px">Portable Restrooms</div>
  <div class="card-text" style="left:460px;top:440px">Lorem ipsum dolor sit amet, consectetur adipiscing elit. Ut elit tellus, luctus nec ullamcorper mattis, pulvinar dapibus leo.</div>
  <div class="read" style="left:500px;top:527px">» READ MORE</div>

  <div class="photo" role="img" aria-label="Bright restroom trailer interior with white vanity" style="left:206px;top:371px;width:195px;height:131px;background:linear-gradient(135deg,#d8d2ca,#f4f2ef 50%,#b9a88f)"></div>
  <div class="card-title" style="left:153px;top:514px">Restroom Trailers</div>
  <div class="card-text" style="left:163px;top:558px">Lorem ipsum dolor sit amet, consectetur adipiscing elit. Ut elit tellus, luctus nec ullamcorper mattis, pulvinar dapibus leo.</div>
  <div class="read" style="left:203px;top:644px">» READ MORE</div>

  <div class="photo" role="img" aria-label="Travel trailer parked on an open grass field under blue sky" style="left:798px;top:371px;width:197px;height:131px;background:linear-gradient(180deg,#6fa6d8 0%,#a9cbe8 55%,#8b8a66 70%,#6c6a4c 100%)"></div>
  <div class="card-title" style="left:747px;top:514px">Travel Trailer</div>
  <div class="card-text" style="left:757px;top:558px">Lorem ipsum dolor sit amet, consectetur adipiscing elit. Ut elit tellus, luctus nec ullamcorper mattis, pulvinar dapibus leo.</div>
  <div class="read" style="left:797px;top:644px">» READ MORE</div>

  <div class="abs" style="left:483px;top:570px;width:238px;height:150px;display:flex;flex-direction:column;align-items:center;justify-content:center;gap:14px">
    <div style="width:70px;height:70px;border-radius:50%;background:var(--gold)"></div>
    <div style="font-family:'Poppins',sans-serif;font-weight:500;font-size:19px;color:var(--gold);white-space:nowrap">VELVET BASIN SUITES</div>
  </div>
  <div class="btn" style="left:515px;top:760px;width:170px;height:38px;font-size:14px"><svg viewBox="0 0 14 14" fill="none" stroke="#fff" stroke-width="2"><path d="M2 3l4 4-4 4M7 3l4 4-4 4"/></svg>CONTACT US</div>
</section>

<section class="abs" style="left:0;top:1568px;width:1200px;height:750px;background:linear-gradient(180deg,#f2f1ef,#f8f8f7 50%,#efeeec)">
  <h2 style="left:0;top:62px;width:1200px;font-size:30px">Why Chose Us?</h2>
  <p class="abs" style="left:180px;top:120px;width:840px;text-align:center;font-size:12px;line-height:20px">We know inviting someone into your home is a big deal. All our professionals are carefully vetted so we choose the right person to care for your home. We guarantee your professional(s) will always be:</p>

  <div class="photo" role="img" aria-label="Businesswoman in black suit holding a folder" style="left:549px;top:186px;width:152px;height:427px;background:linear-gradient(180deg,#d9d6d2,#3a3836 35%,#2a2928)"></div>

  <div class="feat-icon" style="left:173px;top:191px"><svg viewBox="0 0 24 24" fill="none" stroke="#fff" stroke-width="1.5"><circle cx="8" cy="8" r="3"/><circle cx="16" cy="8" r="3"/><path d="M2 20c0-4 3-6 6-6s6 2 6 6M12 20c0-4 2-6 4-6s6 2 6 6"/></svg></div>
  <div class="feat-title" style="left:264px;top:192px">Experienced &amp;<br>Professional</div>
  <div class="feat-text" style="left:264px;top:267px">Select the date and time you'd like your professional to show up.</div>

  <div class="feat-icon" style="left:173px;top:349px"><svg viewBox="0 0 24 24" fill="none" stroke="#fff" stroke-width="1.5"><path d="M12 2l8 3v6c0 5-4 9-8 11-4-2-8-6-8-11V5z"/><path d="M8 12l3 3 5-6"/></svg></div>
  <div class="feat-title" style="left:264px;top:350px">Background &amp; Reference<br>Checked</div>
  <div class="feat-text" style="left:264px;top:425px">Select the date and time you'd like your professional to show up.</div>

  <div class="feat-icon" style="left:173px;top:506px"><svg viewBox="0 0 24 24" fill="none" stroke="#fff" stroke-width="1.5"><path d="M3 4h18v12H8l-5 4z"/><path d="M7 8h10M7 12h7"/></svg></div>
  <div class="feat-title" style="left:264px;top:510px">English Speaking</div>
  <div class="feat-text" style="left:264px;top:553px">Select the date and time you'd like your professional to show up.</div>

  <div class="feat-icon" style="left:948px;top:191px"><svg viewBox="0 0 24 24" fill="none" stroke="#fff" stroke-width="1.5"><circle cx="12" cy="12" r="9"/><path d="M10 8l-1 8M13 9h3M13 12h3M13 15h2"/></svg></div>
  <div class="feat-title right" style="left:736px;top:192px">Interviewed In-Person</div>
  <div class="feat-text right" style="left:771px;top:238px">Select the date and time you'd like your professional to show up.</div>

  <div class="feat-icon" style="left:948px;top:320px"><svg viewBox="0 0 24 24" fill="none" stroke="#fff" stroke-width="1.5"><circle cx="12" cy="7" r="3"/><path d="M6 16c0-3 3-5 6-5s6 2 6 5"/><path d="M4 21l2-2 2 2M16 21l2-2 2 2M10 21l2-2 2 2"/></svg></div>
  <div class="feat-title right" style="left:736px;top:320px">Highly Rated By Other<br>Customers</div>
  <div class="feat-text right" style="left:771px;top:395px">Select the date and time you'd like your professional to show up.</div>

  <div class="feat-icon" style="left:948px;top:477px"><svg viewBox="0 0 24 24" fill="none" stroke="#fff" stroke-width="1.5"><path d="M6 11a6 6 0 0112 0z"/><path d="M4 11h16"/><circle cx="12" cy="15" r="3"/><path d="M5 22c1-3 4-4 7-4s6 1 7 4"/></svg></div>
  <div class="feat-title right" style="left:736px;top:478px">Friendly And Well<br>Mannered</div>
  <div class="feat-text right" style="left:771px;top:553px">Select the date and time you'd like your professional to show up.</div>

  <div class="btn" style="left:868px;top:646px;width:169px;height:38px;font-size:14px"><svg viewBox="0 0 14 14" fill="none" stroke="#fff" stroke-width="2"><path d="M2 3l4 4-4 4M7 3l4 4-4 4"/></svg>CONTACT US</div>
</section>

<section class="abs" style="left:0;top:2318px;width:1200px;height:793px;background:var(--light)">
  <div class="abs" style="left:564px;top:0;width:636px;height:793px;background:var(--dark)"></div>
  <div class="abs" style="left:0;top:30px;width:599px;height:702px;background:var(--white)"></div>
  <div class="photo" role="img" aria-label="Surprised woman in white shirt pointing upward" style="left:152px;top:107px;width:366px;height:617px;background:linear-gradient(180deg,#f3f1ee,#e4e1dc 40%,#2f2e2d 60%,#3a3937)"></div>
  <h2 style="left:274px;top:102px;width:240px;font-size:38px;line-height:48px;font-weight:800">Contact<br>Us</h2>

  <h2 style="left:664px;top:78px;width:380px;font-size:30px;font-weight:800;color:var(--white)">Get A Qutote</h2>
  <p class="abs" style="left:663px;top:134px;width:382px;font-family:'Poppins',sans-serif;font-size:11.5px;line-height:20px;color:var(--white);text-align:justify">Sed ut perspiciatis unde omnis iste natus error sit voluptatem accusantium doloremque laudantium, totam rem aperiam, eaque ipsa quae ab illo inventore veritatis et quasi architecto beatae vitae dicta sunt explicabo. Nemo enim ipsam voluptatem quia voluptas sit.</p>

  <div class="field-label" style="left:663px;top:260px">Name</div>
  <div class="field" style="left:663px;top:277px;width:186px;height:34px">Name</div>
  <div class="field-label" style="left:859px;top:260px">Email</div>
  <div class="field" style="left:859px;top:277px;width:186px;height:34px">Email</div>

  <div class="field-label" style="left:663px;top:325px">Phone</div>
  <div class="field" style="left:663px;top:343px;width:186px;height:34px"></div>
  <div class="field-label" style="left:859px;top:325px">Type Of Event</div>
  <div class="field" style="left:859px;top:343px;width:186px;height:34px"></div>

  <div class="field-label" style="left:663px;top:394px">How Many People?</div>
  <div class="field" style="left:663px;top:419px;width:186px;height:34px"></div>
  <div class="field-label" style="left:859px;top:389px;width:190px;line-height:18px">Type Of Product You Are Interest In?</div>
  <div class="field" style="left:859px;top:425px;width:186px;height:30px;justify-content:space-between;color:#555">Restroom Trailers<svg width="8" height="6"><path d="M0 0h8L4 5z" fill="var(--gold)"/></svg></div>

  <div class="field-label" style="left:663px;top:469px">When You Need It?</div>
  <div class="field" style="left:663px;top:486px;width:186px;height:34px"></div>
  <div class="field-label" style="left:859px;top:469px">For How Long? (In Hours)</div>
  <div class="field" style="left:859px;top:486px;width:186px;height:34px"></div>

  <div class="field-label" style="left:663px;top:533px">Where?</div>
  <div class="field" style="left:663px;top:550px;width:382px;height:34px"></div>

  <div class="field-label" style="left:663px;top:597px">Message</div>
  <div class="field" style="left:663px;top:616px;width:382px;height:73px"></div>

  <div class="btn" style="left:761px;top:700px;width:184px;height:29px;font-size:9px;font-weight:600;letter-spacing:1px"><svg viewBox="0 0 14 14" style="width:10px;height:10px"><rect x="1" y="3" width="12" height="8" fill="#fff"/><path d="M1 3l6 4 6-4" stroke="var(--gold)" fill="none"/></svg>SEND YOUR MESSAGE</div>
</section>

<section class="abs" style="left:0;top:3111px;width:1200px;height:499px;background:linear-gradient(90deg,#f6f5f3,#faf9f8)">
  <h2 style="left:151px;top:70px;width:600px;font-size:31px;text-align:center">Check What Our Clients Say</h2>
  <div class="abs" style="left:192px;top:137px;width:519px;height:115px;background:var(--gold);border-radius:6px;display:flex;align-items:center;justify-content:center;padding:0 50px;text-align:center;font-family:'Poppins',sans-serif;font-style:italic;font-size:13px;line-height:20px;color:var(--white)">"Lorem ipsum dolor sit amet, consectetur adipiscing elit. Ut elit tellus, luctus nec ullamcorper mattis, pulvinar dapibus leo."</div>
  <svg class="abs" style="left:441px;top:251px" width="20" height="10"><path d="M0 0h20L10 10z" fill="var(--gold)"/></svg>
  <div class="photo" role="img" aria-label="Client portrait in a round frame" style="left:363px;top:273px;width:116px;height:116px;border-radius:50%;background:linear-gradient(180deg,#7a6a5c,#3f3833)"></div>
  <div class="abs" style="left:496px;top:316px;font-family:'Poppins',sans-serif;font-size:10.5px;line-height:17px;color:var(--dark)">John Doe<br><span style="color:#777">CEO</span></div>
  <svg class="abs" style="left:164px;top:255px" width="10" height="16" fill="none" stroke="var(--gold)" stroke-width="2"><path d="M8 2L2 8l6 6"/></svg>
  <svg class="abs" style="left:728px;top:255px" width="10" height="16" fill="none" stroke="var(--gold)" stroke-width="2"><path d="M2 2l6 6-6 6"/></svg>
  <div class="abs" style="left:400px;top:415px;display:flex;gap:10px">
    <span style="width:12px;height:12px;border-radius:50%;background:#c8c8c8"></span>
    <span style="width:12px;height:12px;border-radius:50%;background:#c8c8c8"></span>
    <span style="width:12px;height:12px;border-radius:50%;background:var(--gold)"></span>
    <span style="width:12px;height:12px;border-radius:50%;background:#c8c8c8"></span>
    <span style="width:12px;height:12px;border-radius:50%;background:#c8c8c8"></span>
  </div>
  <div class="photo" role="img" aria-label="Smiling businesswoman in black blazer pointing left" style="left:755px;top:30px;width:312px;height:469px;background:linear-gradient(180deg,#7a5340 0%,#d9c3b0 25%,#2a2928 45%,#1f1e1d 100%)"></div>
</section>

<footer class="abs" style="left:0;top:3610px;width:1200px;height:319px">
  <div class="abs" style="left:0;top:0;width:1200px;height:91px;background:var(--dark)"></div>
  <div class="brand-box" style="left:41px;top:0;width:116px;height:91px"><div class="dot"></div><div class="name">VELVET BASIN<br>SUITES</div></div>
  <nav class="nav" style="left:0;top:27px">
    <span class="active" style="left:400px">HOME</span>
    <span style="left:473px">ABOUT US</span>
    <span style="left:575px">OUR PRODUCTS</span>
    <span style="left:714px">CONTACT US</span>
  </nav>
  <div class="abs" style="left:1039px;top:18px;width:36px;height:36px;border-radius:50%;background:var(--gold)"></div>
  <div class="abs" style="left:1082px;top:18px;width:36px;height:36px;border-radius:50%;background:var(--gold)"></div>
  <div class="abs" style="left:1124px;top:18px;width:36px;height:36px;border-radius:50%;background:var(--gold)"></div>
  <div class="abs" style="left:0;top:91px;width:1200px;height:9px;background:var(--gold)"></div>

  <div class="abs" style="left:0;top:100px;width:1200px;height:128px;background:var(--light)"></div>
  <div class="info-title" style="left:226px;top:123px">Call Us</div>
  <div class="info-icon" style="left:175px;top:158px"><svg viewBox="0 0 24 24" fill="#fff"><path d="M6.6 10.8a15 15 0 006.6 6.6l2.2-2.2c.3-.3.7-.4 1-.2 1.1.4 2.3.6 3.6.6.6 0 1 .4 1 1V20c0 .6-.4 1-1 1A17 17 0 013 4c0-.6.4-1 1-1h3.5c.6 0 1 .4 1 1 0 1.3.2 2.5.6 3.6.1.3 0 .7-.2 1z"/></svg></div>
  <div class="info-text" style="left:226px;top:167px">+1 (555) 014-2290</div>

  <div class="info-title" style="left:476px;top:123px">Email Us</div>
  <div class="info-icon" style="left:425px;top:158px"><svg viewBox="0 0 24 24"><rect x="2" y="5" width="20" height="14" rx="2" fill="#fff"/><path d="M2 6l10 7 10-7" stroke="var(--gold)" stroke-width="1.5" fill="none"/></svg></div>
  <div class="info-text" style="left:476px;top:167px">info@VelvetBasinSuites.com</div>

  <div class="info-title" style="left:805px;top:123px">Find Us</div>
  <div class="info-icon" style="left:756px;top:181px"><svg viewBox="0 0 24 24" fill="#fff"><path d="M12 2a7 7 0 00-7 7c0 5 7 13 7 13s7-8 7-13a7 7 0 00-7-7zm0 9.5a2.5 2.5 0 110-5 2.5 2.5 0 010 5z"/></svg></div>
  <div class="info-text" style="left:805px;top:167px">#48 Velvet Basin Suites, Linden Court,<br>Oregon</div>

  <div class="abs" style="left:0;top:228px;width:1200px;height:91px;background:var(--dark);display:flex;align-items:center;justify-content:center;font-family:'Poppins',sans-serif;font-size:11.5px;color:var(--white)">Copyright © 2022 Velvet Basin Suites | Powered by Velvet Basin Suites</div>
</footer>

</body>
</html>
```